Letter Head / Envelopes
Business Card
Professional
Glen Hartwick Sr
Managing Partner
418 Tamsin Rd Fernbrook, PA 19990
glen@copperfieldre.com
www.copperfieldre.com

```html
<!DOCTYPE html>
<html lang="en">
<head>
<meta charset="utf-8">
<title>Copperfield Real Estate — Stationery</title>
<link rel="stylesheet" href="https://fonts.googleapis.com/css2?family=Libre+Baskerville:wght@700&family=Arimo:wght@400;700&display=swap">
<style>
  :root {
    --backdrop: #1c1b1a;
    --paper: #ffffff;
    --card-dark: #161412;
    --brand-red: #8e1d1f;
    --ink: #3a3a3a;
    --ink-light: #f0ece6;
    --faint: #e6e6e6;
    --accent-tan: #b08a5a;
    --mark: #2b2623;
    --curve-paper: #f4f1ec;
  }
  * { margin: 0; padding: 0; box-sizing: border-box; }
  html, body { width: 1200px; height: 804px; overflow: hidden; }
  body {
    background: var(--backdrop);
    position: relative;
    font-family: "Arimo", Arial, sans-serif;
    color: var(--ink);
  }
  .piece { position: absolute; background: var(--paper); }

  .brand {
    display: flex; align-items: center; gap: 8px;
    font-family: "Libre Baskerville", Georgia, serif;
    font-weight: 700; color: var(--brand-red);
    text-transform: uppercase; line-height: 1.05;
  }
  .brand-square { background: var(--mark); flex: none; }
  .brand-name { display: block; }

  .contact { font-size: 8px; line-height: 1.45; }

  /* Letterhead */
  .letterhead { left: 53px; top: 34px; width: 504px; height: 489px; }
  .letterhead .brand { position: absolute; left: 28px; top: 40px; font-size: 15px; }
  .letterhead .brand-square { width: 22px; height: 22px; }
  .letterhead .contact { position: absolute; left: 334px; top: 30px; }
  .letterhead .contact .gap { margin-top: 7px; }
  .watermark {
    position: absolute; left: 0; right: 0; top: 210px; text-align: center;
    font-family: "Libre Baskerville", Georgia, serif; font-weight: 700;
    font-size: 40px; line-height: 1.15; color: var(--faint); text-transform: uppercase;
  }

  /* Dark business cards (top) */
  .card-dark {
    top: 29px; width: 138px; height: 120px; background: var(--card-dark);
    overflow: hidden;
  }
  .card-dark.one { left: 600px; }
  .card-dark.two { left: 752px; }
  .card-dark .curve { position: absolute; left: 0; top: 0; width: 52px; height: 120px; }
  .card-dark .side-brand {
    position: absolute; left: 6px; top: 98px; transform-origin: left top;
    transform: rotate(-90deg); font-size: 8px; white-space: nowrap;
    color: var(--brand-red);
  }
  .card-dark .person { position: absolute; left: 64px; top: 12px; font-size: 7px; color: var(--accent-tan); line-height: 1.4; }
  .card-dark .person b { display: block; }
  .card-dark .contact { position: absolute; left: 64px; top: 46px; font-size: 6px; color: var(--ink-light); }

  /* Envelope front */
  .envelope { left: 581px; top: 180px; width: 576px; height: 353px; }
  .envelope .brand { position: absolute; left: 42px; top: 36px; font-size: 13px; }
  .envelope .brand-square { width: 18px; height: 18px; }
  .envelope .watermark { top: 80px; left: 150px; right: auto; font-size: 17px; text-align: left; }
  .envelope .contact { position: absolute; left: 42px; top: 274px; }

  /* Envelope back */
  .envelope-back { left: 581px; top: 552px; width: 576px; height: 216px; overflow: hidden; }
  .envelope-back .flap { position: absolute; inset: 0; }
  .envelope-back .brand { position: absolute; left: 232px; top: 50px; font-size: 12px; }
  .envelope-back .brand-square { width: 16px; height: 16px; }

  /* Business cards (bottom left) */
  .card-front-dark { left: 250px; top: 552px; width: 230px; height: 120px; background: var(--card-dark); }
  .card-front-dark .brand { position: absolute; left: 26px; top: 40px; font-size: 15px; }
  .card-front-dark .brand-square { width: 22px; height: 22px; background: var(--accent-tan); }
  .card-front-light { left: 250px; top: 684px; width: 230px; height: 104px; }
  .card-front-light .brand { position: absolute; left: 26px; top: 34px; font-size: 15px; }
  .card-front-light .brand-square { width: 22px; height: 22px; }
</style>
</head>
<body>

<section class="piece letterhead" aria-label="Letterhead">
  <div class="brand"><span class="brand-square"></span><span class="brand-name">Copperfield<br>Real Estate</span></div>
  <div class="contact">
    418 Tamsin Rd<br>Fernbrook, PA 19990
    <div class="gap">Phone: 555-310-4827<br>Cell: 555-310-6194<br>Fax: 555-310-7350</div>
  </div>
  <div class="watermark">Copperfield<br>Real Estate</div>
</section>

<section class="piece card-dark one" aria-label="Business card back">
  <svg class="curve" viewBox="0 0 52 120" preserveAspectRatio="none"><path d="M0 0 H30 Q52 60 30 120 H0 Z" fill="var(--curve-paper)"/><path d="M30 0 Q52 60 30 120" fill="none" stroke="var(--accent-tan)" stroke-width="2"/></svg>
  <span class="side-brand brand"><span class="brand-name">Copperfield<br>Real Estate</span></span>
  <div class="person"><b>Glen Hartwick Sr</b>Managing Partner</div>
  <div class="contact">418 Tamsin Rd<br>Fernbrook, PA 19990<br><br>Phone: 555-310-4827<br>Cell: 555-310-6194<br>Fax: 555-310-7350<br>glen@copperfieldre.com<br>www.copperfieldre.com</div>
</section>

<section class="piece card-dark two" aria-label="Business card back">
  <svg class="curve" viewBox="0 0 52 120" preserveAspectRatio="none"><path d="M0 0 H30 Q52 60 30 120 H0 Z" fill="var(--curve-paper)"/><path d="M30 0 Q52 60 30 120" fill="none" stroke="var(--accent-tan)" stroke-width="2"/></svg>
  <span class="side-brand brand"><span class="brand-name">Copperfield<br>Real Estate</span></span>
  <div class="person"><b>Glen Hartwick Sr</b>Managing Partner</div>
  <div class="contact">418 Tamsin Rd<br>Fernbrook, PA 19990<br><br>Phone: 555-310-4827<br>Cell: 555-310-6194<br>Fax: 555-310-7350<br>glen@copperfieldre.com<br>www.copperfieldre.com</div>
</section>

<section class="piece envelope" aria-label="Envelope front">
  <div class="brand"><span class="brand-square"></span><span class="brand-name">Copperfield<br>Real Estate</span></div>
  <div class="watermark">Copperfield<br>Real Estate</div>
  <div class="contact">418 Tamsin Rd<br>Fernbrook, PA 19990<br><br>Phone: 555-310-4827<br>Cell: 555-310-6194<br>Fax: 555-310-7350</div>
</section>

<section class="piece envelope-back" aria-label="Envelope back">
  <svg class="flap" viewBox="0 0 576 216" preserveAspectRatio="none">
    <path d="M0 0 L288 120 L576 0" fill="none" stroke="#cfcfcf" stroke-width="1.5"/>
    <path d="M0 216 L250 110 M576 216 L326 110" fill="none" stroke="#e2e2e2" stroke-width="1"/>
  </svg>
  <div class="brand"><span class="brand-square"></span><span class="brand-name">Copperfield<br>Real Estate</span></div>
</section>

<section class="piece card-front-dark" aria-label="Business card front, dark">
  <div class="brand"><span class="brand-square"></span><span class="brand-name">Copperfield<br>Real Estate</span></div>
</section>

<section class="piece card-front-light" aria-label="Business card front, light">
  <div class="brand"><span class="brand-square"></span><span class="brand-name">Copperfield<br>Real Estate</span></div>
</section>

</body>
</html>
```